Diversity report of banking market in Europe

*Power point presentation style - rather than corporate brochure*
We are an executive recruitment firm who will be sending a report to all our senior clients. We need a designer to make it look eye catching, slick and professional for our audience. The document will be read mainly by PDF so the type of font and size will be very important as will the size of each page.

We have all the content but may need guidance on the amount of text, the size of graphs and inserting some pictures/vectors etc. We can provide more text or cut text back it it helps the design. We can find more graphs if this helps to fill a page

Industry/Entity Type

Investment Banking

Font styles to use
Sans Serif

Colors
0255a3
33b8a4
85cae6
cfeae6
ffffff

Requirements
Must have
• Colours:
11, 29, 49
70, 165, 175
Nice to have
• Have added two example Marvenholt documents that we feel are clean and professional. Please use these are our attempt as a guide line to how was want the document to look and feel and flow. Happy to add additional pictures or design to fill out pages. Cant steal actual pictures from marvenholt report

```html
<!DOCTYPE html>
<html lang="en">
<head>
<meta charset="utf-8">
<title>Diversity in European Credit – Gender and Ethnicity</title>
<link rel="stylesheet" href="https://fonts.googleapis.com/css2?family=Lato:ital,wght@0,400;0,700;1,400;1,700&family=Roboto+Slab:wght@400;500&display=swap">
<style>
  :root {
    --ink: #1d1d1f;
    --teal: #1fa89a;
    --blue: #1f57a0;
    --pink: #ec4f96;
    --pink-light: #f38aaa;
    --purple: #6a3f98;
    --violet: #8a3c9a;
    --grid: #e3e3e6;
    --paper: #ffffff;
    --centre: #f8fafd;
  }
  * { margin: 0; padding: 0; box-sizing: border-box; }
  html, body { width: 1200px; height: 848px; overflow: hidden; background: var(--paper); }
  .page { position: relative; width: 1200px; height: 848px; font-family: "Lato", Arial, sans-serif; color: var(--ink); }

  .intro {
    position: absolute; left: 51px; top: 14px; width: 1100px;
    font-style: italic; font-size: 15px; line-height: 21.5px; text-indent: 8px;
  }

  .donut { position: absolute; left: 150px; top: 181px; }
  .donut-value {
    position: absolute; font-family: "Roboto Slab", Georgia, serif;
    font-size: 34px; letter-spacing: 1px;
  }
  .donut-value.male { left: 106px; top: 196px; color: var(--purple); }
  .donut-value.female { left: 440px; top: 470px; color: var(--pink-light); }

  .bar-chart { position: absolute; left: 640px; top: 165px; }

  .legend-item { position: absolute; top: 459px; }
  .legend-figure { position: absolute; left: 0; top: 0; width: 38px; height: 106px; border-radius: 16px 16px 6px 6px; }
  .legend-value {
    position: absolute; left: 52px; top: 29px;
    font-family: "Roboto Slab", Georgia, serif; font-size: 25px; white-space: nowrap;
  }
  .legend-value span { font-size: 18px; }
  .legend-note {
    position: absolute; left: 52px; top: 66px; width: 62px;
    font-size: 6px; line-height: 8.5px; color: #555;
  }

  .section-title {
    position: absolute; top: 622px;
    font-style: italic; font-size: 24px; color: var(--teal); font-weight: 400;
  }
  .section-body {
    position: absolute; top: 678px; width: 540px;
    font-style: italic; font-size: 15.5px; line-height: 27px; text-indent: 8px;
  }
</style>
</head>
<body>
<div class="page">

  <p class="intro">The overall gender diversity levels across each strategy will be explored further in this report. The below chart is a clear visualisation of male to female ratio's for Investment Professionals working in Direct Lending, Single Name Distressed, CLOs and Leveraged Finance. Direct Lending as an asset class has the closest male to female diversity ratio as found in banking. We are tracking a 17% gender diversity in Banking and a 14% gender diversity in Direct Lending.</p>

  <svg class="donut" width="316" height="316" viewBox="0 0 316 316" role="img" aria-label="Donut chart: 60% male, 40% female">
    <defs>
      <linearGradient id="pinkArc" x1="0" y1="0" x2="0.3" y2="1">
        <stop offset="0" stop-color="#f48ba6"/>
        <stop offset="1" stop-color="#e92f8a"/>
      </linearGradient>
      <linearGradient id="maleIcon" x1="0" y1="0" x2="0" y2="1">
        <stop offset="0" stop-color="#1f57a0"/>
        <stop offset="1" stop-color="#1a4a8c"/>
      </linearGradient>
      <linearGradient id="femaleIcon" x1="0" y1="0" x2="0" y2="1">
        <stop offset="0" stop-color="#f07aa4"/>
        <stop offset="1" stop-color="#e8358c"/>
      </linearGradient>
    </defs>
    <!-- 60% segment -->
    <path d="M158 0 A158 158 0 1 0 250.9 285.8 L230.3 257.5 A123 123 0 1 1 158 35 Z" fill="var(--blue)"/>
    <!-- 40% segment -->
    <path d="M158 0 A158 158 0 0 1 250.9 285.8 L230.3 257.5 A123 123 0 0 0 158 35 Z" fill="url(#pinkArc)"/>
    <circle cx="158" cy="158" r="123" fill="var(--centre)"/>
    <rect x="105" y="108" width="40" height="112" rx="14" fill="url(#maleIcon)" role="img" aria-label="Male figure icon"/>
    <rect x="168" y="108" width="44" height="112" rx="14" fill="url(#femaleIcon)" role="img" aria-label="Female figure icon"/>
  </svg>
  <div class="donut-value male">60%</div>
  <div class="donut-value female">40%</div>

  <svg class="bar-chart" width="460" height="285" viewBox="0 0 460 285" role="img" aria-label="Bar chart of five strategies, each bar topped by a person figure">
    <defs>
      <linearGradient id="bar1" x1="0" y1="0" x2="0" y2="1"><stop offset="0" stop-color="#f9b233"/><stop offset="1" stop-color="#f26a3a"/></linearGradient>
      <linearGradient id="bar2" x1="0" y1="0" x2="0" y2="1"><stop offset="0" stop-color="#f06aa6"/><stop offset="1" stop-color="#e72f8a"/></linearGradient>
      <linearGradient id="bar3" x1="0" y1="0" x2="0" y2="1"><stop offset="0" stop-color="#d060a8"/><stop offset="1" stop-color="#9b3b9e"/></linearGradient>
      <linearGradient id="bar4" x1="0" y1="0" x2="0" y2="1"><stop offset="0" stop-color="#7e4a9e"/><stop offset="1" stop-color="#4f4fa0"/></linearGradient>
      <linearGradient id="bar5" x1="0" y1="0" x2="0" y2="1"><stop offset="0" stop-color="#8a3c9a"/><stop offset="1" stop-color="#5c2f8e"/></linearGradient>
    </defs>
    <g stroke="var(--grid)" stroke-width="1">
      <line x1="3" y1="5" x2="454" y2="5"/><line x1="3" y1="24" x2="454" y2="24"/>
      <line x1="3" y1="43" x2="454" y2="43"/><line x1="3" y1="62" x2="454" y2="62"/>
      <line x1="3" y1="81" x2="454" y2="81"/><line x1="3" y1="100" x2="454" y2="100"/>
      <line x1="3" y1="119" x2="454" y2="119"/><line x1="3" y1="138" x2="454" y2="138"/>
      <line x1="3" y1="157" x2="454" y2="157"/><line x1="3" y1="176" x2="454" y2="176"/>
      <line x1="3" y1="195" x2="454" y2="195"/><line x1="3" y1="214" x2="454" y2="214"/>
      <line x1="3" y1="233" x2="454" y2="233"/><line x1="3" y1="252" x2="454" y2="252"/>
      <line x1="3" y1="271" x2="454" y2="271"/>
      <line x1="3" y1="5" x2="3" y2="276"/>
    </g>
    <rect x="49" y="198" width="57" height="78" fill="url(#bar1)"/>
    <rect x="125" y="160" width="57" height="116" fill="url(#bar2)"/>
    <rect x="202" y="102" width="56" height="174" fill="url(#bar3)"/>
    <rect x="277" y="140" width="56" height="136" fill="url(#bar4)"/>
    <rect x="351" y="122" width="57" height="154" fill="url(#bar5)"/>
    <g>
      <rect x="66" y="100" width="22" height="80" rx="9" fill="url(#bar1)" role="img" aria-label="Person figure"/>
      <rect x="142" y="62" width="22" height="80" rx="9" fill="url(#bar2)" role="img" aria-label="Person figure"/>
      <rect x="219" y="4" width="22" height="80" rx="9" fill="url(#bar3)" role="img" aria-label="Person figure"/>
      <rect x="294" y="42" width="22" height="80" rx="9" fill="url(#bar4)" role="img" aria-label="Person figure"/>
      <rect x="369" y="24" width="22" height="80" rx="9" fill="url(#bar5)" role="img" aria-label="Person figure"/>
    </g>
  </svg>

  <div class="legend-item" style="left:696px">
    <div class="legend-figure" style="background:linear-gradient(#d064a8,#a0469e)" role="img" aria-label="Person figure"></div>
    <div class="legend-value" style="color:#c4539f">50<span>%</span></div>
    <p class="legend-note">Lorem ipsum dolor sit amet, consectetur adipiscing elit.</p>
  </div>
  <div class="legend-item" style="left:816px">
    <div class="legend-figure" style="background:linear-gradient(#6a4a9e,#4f4a9a)" role="img" aria-label="Person figure"></div>
    <div class="legend-value" style="color:#4f4a9a">25<span>%</span></div>
    <p class="legend-note">Lorem ipsum dolor sit amet, consectetur adipiscing elit.</p>
  </div>
  <div class="legend-item" style="left:937px">
    <div class="legend-figure" style="background:linear-gradient(#7a3a98,#5c2f8e)" role="img" aria-label="Person figure"></div>
    <div class="legend-value" style="color:#6a3594">25<span>%</span></div>
    <p class="legend-note">Lorem ipsum dolor sit amet, consectetur adipiscing elit.</p>
  </div>

  <h2 class="section-title" style="left:51px">Female to Male Ratio</h2>
  <p class="section-body" style="left:51px">There are currently 5714 professionals working across Direct Lending, Single Name Distressed, CLOs and Leveraged Finance in Europe. 805 (14%) are female and 4909 (86%) are male</p>

  <h2 class="section-title" style="left:621px">Ethnic to White Ratio</h2>
  <p class="section-body" style="left:621px">672 investment professionals working in across Direct Lending, Single Name Distressed, CLOs and Leveraged Finance in Europe fall within Ethnic Minorities whereas 5042 of the work force is White</p>

</div>
</body>
</html>
```